Golf Charity Classic Tournament

We need an upscale golf flyer for a business related annual golf tournament at a local country club.

I attached our flyer from last year to give you an idea of the information.
This flyer is missing a sponsor area so please leave an area for our sponsor logos.

The name of the tournament is the BRV Pathfinders Charity Classic.

For flyer details...
BRV Pathfinders Charity Classic, 11am registration, noon shotgun, Monday, November 9th, Thornhaven Country Club, see address on attached flyer.

Cost/membership info? $175 per player, $350 for twosome, or $600 on a foursome

Charity or cause? The Open Green of Greater Dallas

Any other important details? New features: Leaderboard and Caddie Club Leave bottom area for white/blank for sponsors

Digital or print? Digital jpeg file, but will need printable as well.

We will need logos added to flyer upon request until our event.

Thank you.

Target Market(s)

25-55 Corporate and Finance professionals for a business golf tournament that partners with Open Green charity

Industry/Entity Type

Business

Font styles to use
Serif

Requirements
Nice to have
• The flyer should be bold and stand out...Looking for creative design in the layout, use of color and fonts.
Should not have
• Boring golf appeal

```html
<!DOCTYPE html>
<html lang="en">
<head>
<meta charset="utf-8">
<title>BRV Pathfinders Charity Classic – 12th Annual Golf Tournament</title>
<link href="https://fonts.googleapis.com/css2?family=Playfair+Display:wght@700;900&family=Lora:wght@500;600;700&display=swap" rel="stylesheet">
<style>
  :root {
    --green: #6cb52d;
    --green-dark: #3c8419;
    --green-light: #a5d655;
    --ink: #333333;
    --muted: #8a8a8a;
    --rule: #d9d9d9;
    --white: #ffffff;
  }
  * { margin: 0; padding: 0; box-sizing: border-box; }
  html, body { width: 900px; height: 1200px; overflow: hidden; background: var(--white); }
  body { font-family: "Lora", Georgia, serif; color: var(--ink); }
  .flyer { position: relative; width: 900px; height: 1200px; background: var(--white); overflow: hidden; }
  .display { font-family: "Playfair Display", Georgia, serif; }

  .header { position: absolute; top: 0; left: 0; width: 900px; height: 178px; }
  .header-rule { position: absolute; left: 0; top: 150px; width: 900px; height: 40px; }
  .classic-mark { position: absolute; left: 50px; top: 34px; display: flex; align-items: center; gap: 14px; }
  .classic-mark .dot { width: 34px; height: 34px; border-radius: 50%; background: var(--green); }
  .classic-mark .name { font-family: "Playfair Display", Georgia, serif; font-weight: 700; font-size: 32px; color: var(--green-dark); line-height: 1.05; }
  .title { position: absolute; right: 50px; top: 28px; text-align: left; }
  .title .edition { font-size: 60px; font-weight: 900; color: var(--green); line-height: 1; letter-spacing: 0.5px; }
  .title .event { font-size: 44px; font-weight: 700; color: var(--ink); line-height: 1.1; margin-top: 6px; }

  .hero-photo { position: absolute; top: 178px; left: 0; width: 900px; height: 380px;
    background:
      radial-gradient(ellipse 340px 220px at 78% 18%, rgba(255,250,220,0.85), rgba(255,250,220,0) 70%),
      linear-gradient(180deg, #dff0c4 0%, #b6da7c 30%, #78b236 58%, #3f7d1a 100%); }
  .swoosh { position: absolute; top: 440px; left: 0; width: 900px; height: 150px; }

  .info-panel { position: absolute; top: 505px; left: 560px; width: 340px; height: 580px;
    background: linear-gradient(180deg, var(--green-light) 0%, var(--green) 40%, var(--green-dark) 100%);
    color: var(--white); text-align: center; }
  .bag-photo { width: 200px; height: 200px; border-radius: 50%; margin: 22px auto 0;
    border: 6px solid var(--white);
    background: radial-gradient(circle at 40% 35%, #eaf5d2 0%, #a9d461 40%, #4d8f22 100%); }
  .registration-time { font-size: 36px; font-weight: 700; margin-top: 22px; }
  .prices { font-size: 20px; font-weight: 600; line-height: 1.5; margin-top: 12px; }
  .register-label { font-size: 36px; font-weight: 700; margin-top: 24px; }
  .register-url { font-size: 19px; font-weight: 600; margin-top: 4px; }
  .register-venue { font-size: 20px; font-weight: 600; margin-top: 12px; }

  .event-name { position: absolute; left: 32px; top: 588px; font-size: 44px; font-weight: 900;
    color: var(--green); line-height: 1.12; }
  .charity-bar { position: absolute; left: 0; top: 702px; width: 540px; height: 50px;
    background: var(--green); color: var(--white); font-size: 23px; font-weight: 600;
    padding-left: 32px; line-height: 50px; }
  .details { position: absolute; left: 40px; top: 772px; list-style: none; font-size: 22px;
    font-weight: 600; line-height: 1.55; color: var(--ink); }
  .details li::before { content: "•"; color: var(--green); margin-right: 10px; }

  .partners { position: absolute; left: 36px; top: 935px; display: flex; flex-direction: column; gap: 30px; }
  .partner { display: flex; align-items: center; gap: 12px; font-size: 28px; font-weight: 700; color: var(--green-dark); }
  .partner .dot { width: 22px; height: 22px; border-radius: 50%; background: var(--green); }
  .golfer-photo { position: absolute; left: 320px; top: 880px; width: 240px; height: 205px;
    background:
      radial-gradient(ellipse 120px 80px at 55% 30%, rgba(255,255,255,0.7), rgba(255,255,255,0) 70%),
      linear-gradient(180deg, #a9d2ee 0%, #d4e9e6 52%, #8cc04e 70%, #4f8f25 100%); }

  .sponsor-band { position: absolute; left: 0; top: 1085px; width: 900px; height: 115px;
    background: var(--white); border-top: 6px solid var(--green);
    color: var(--muted); text-align: center;
    font-size: 22px; font-weight: 700; line-height: 109px; letter-spacing: 2px; }
</style>
</head>
<body>
<div class="flyer">
  <header class="header">
    <div class="classic-mark"><span class="dot"></span><span class="name">BRV<br>Classic</span></div>
    <div class="title display">
      <div class="edition">12TH ANNUAL</div>
      <div class="event">GOLF TOURNAMENT</div>
    </div>
  </header>

  <div class="hero-photo" role="img" aria-label="Close-up of a gloved hand placing a golf ball on a tee beside an iron on a sunlit fairway"></div>
  <svg class="header-rule" viewBox="0 0 900 40" aria-hidden="true">
    <path d="M0 28 C 300 0, 600 0, 900 28 L900 40 L0 40 Z" fill="#ffffff" opacity="0"/>
  </svg>
  <svg class="swoosh" viewBox="0 0 900 150" aria-hidden="true">
    <path d="M0 70 C 250 150, 550 20, 900 40 L900 150 L0 150 Z" fill="#ffffff"/>
    <path d="M0 58 C 260 140, 560 8, 900 26 L900 42 C 560 26, 260 150, 0 78 Z" fill="#6cb52d"/>
    <path d="M0 92 C 260 160, 560 40, 900 56 L900 63 C 560 48, 260 168, 0 101 Z" fill="#a5d655"/>
  </svg>

  <aside class="info-panel">
    <div class="bag-photo" role="img" aria-label="Golf bag with clubs resting on the course"></div>
    <div class="registration-time display">11am registration</div>
    <div class="prices">$175 PER PLAYER<br>$350 FOR TWOSOME or<br>$600 ON A FOURSOME</div>
    <div class="register-label display">Registration at</div>
    <div class="register-url">www.brvgroup.org/dfw/events</div>
    <div class="register-venue">Thornhaven Country Club</div>
  </aside>

  <h1 class="event-name display">BRV PATHFINDERS<br>CHARITY CLASSIC</h1>
  <div class="charity-bar">The Open Green of Greater Dallas</div>
  <ul class="details">
    <li>Shotgun at noon</li>
    <li>Monday, November 9th</li>
    <li>Thornhaven Country Club</li>
  </ul>

  <div class="partners">
    <div class="partner"><span class="dot"></span>Open Green</div>
    <div class="partner"><span class="dot"></span>Bogey Club</div>
  </div>
  <div class="golfer-photo" role="img" aria-label="Golfer mid-swing against a blue sky above the green"></div>

  <footer class="sponsor-band">---- SPONSOR LOGOS ----</footer>
</div>
</body>
</html>
```